Comp & Pen Prep Tip Sheet for Veterans

I need a flyer/brochure/card with tips to help prepare veterans for their upcoming Comp & Pen Exams. Needs to be colorful and have vectors/images that correspond with teach tip. I have attached a word document with the language to include. This will go out with our welcome kit for veterans to reference before their exam.

Target Market(s)

Veterans

Industry/Entity Type

Legal/Non-Profit Organization/Medical

Colors
0054AA
0677BA
7BADD7
CADEEF
E8F1F8

Requirements
Must have
• Vectors/easy to follow

```html
<!DOCTYPE html>
<html lang="en">
<head>
<meta charset="utf-8">
<title>The Comp &amp; Pen Exam – Tip Sheet</title>
<link href="https://fonts.googleapis.com/css2?family=Oswald:wght@500;600&family=Saira+Semi+Condensed:wght@400;600;700&display=swap" rel="stylesheet">
<style>
  :root{
    --backdrop:#1c1c1c;
    --paper:#ffffff;
    --navy:#0d4a9c;
    --navy-deep:#0a3a7e;
    --crimson:#9c1c20;
    --ink:#1f1f1f;
    --card:#d8d8d8;
    --band:#0a0a0a;
    --photo-a:#e9eee9;
    --photo-b:#b9c4b6;
    --photo-c:#6f7a5f;
  }
  *{margin:0;padding:0;box-sizing:border-box}
  html,body{width:1200px;height:1177px;overflow:hidden;background:var(--backdrop)}
  body{position:relative;font-family:"Saira Semi Condensed",sans-serif;color:var(--ink)}
  .flyer{position:absolute;left:254px;top:82px;width:720px;height:1018px;background:var(--paper);overflow:hidden}
  .hero-art{position:absolute;left:0;top:0}
  .brand-seal{position:absolute;left:79px;top:68px;width:156px;height:156px;border-radius:50%;background:var(--paper);
    border:5px solid var(--navy);display:flex;align-items:center;justify-content:center;text-align:center;
    font-family:"Saira Semi Condensed",sans-serif;font-weight:700;font-size:19px;line-height:1.15;color:var(--navy);padding:18px}
  .intro-panel{position:absolute;left:17px;top:282px;width:279px;text-align:center;color:#fff}
  .intro-lead{font-weight:600;font-size:15px;line-height:19px;padding:0 28px}
  .intro-note{margin:26px 17px 0;background:var(--navy-deep);font-weight:600;font-size:15px;line-height:19px;padding:9px 10px 8px}
  .exam-summary{position:absolute;left:331px;top:345px;width:372px;font-size:13px;line-height:16px;text-align:justify}
  .exam-summary p+p{margin-top:12px}
  .section-band{position:absolute;left:0;top:509px;width:720px;height:43px;background:var(--band);display:flex;align-items:center;justify-content:center;gap:18px}
  .section-band::before,.section-band::after{content:"";width:108px;height:3px;background:var(--crimson)}
  .section-band h2{font-family:"Oswald",sans-serif;font-weight:500;font-size:27px;color:#fff;letter-spacing:.3px}
  .tips{position:absolute;left:17px;top:566px;width:685px;display:grid;grid-template-columns:221px 224px 224px;grid-template-rows:214px 216px;column-gap:8px;row-gap:10px}
  .tip{background:var(--card);padding:6px 7px 0 7px}
  .tip-head{display:flex;align-items:center;height:46px;margin-bottom:4px}
  .tip-icon{width:48px;height:40px;flex:none}
  .tip h3{font-family:"Oswald",sans-serif;font-weight:500;font-size:19px;line-height:19px;text-transform:uppercase;margin-left:12px}
  .tip.blue h3{color:var(--navy)}
  .tip.red h3{color:var(--crimson)}
  .tip p{font-size:12px;line-height:14.5px;text-align:justify}
  .tip p+p{margin-top:13px}
</style>
</head>
<body>
<main class="flyer">
  <svg class="hero-art" width="720" height="500" viewBox="0 0 720 500">
    <defs>
      <linearGradient id="photoTone" x1="0" y1="0" x2="1" y2="1">
        <stop offset="0" stop-color="var(--photo-a)"/>
        <stop offset=".55" stop-color="var(--photo-b)"/>
        <stop offset="1" stop-color="var(--photo-c)"/>
      </linearGradient>
    </defs>
    <polygon points="0,0 720,0 720,196 0,300" fill="url(#photoTone)" role="img" aria-label="Photo of a uniformed service member speaking with a medical examiner holding a clipboard"/>
    <polygon points="0,296 720,196 720,266 0,366" fill="var(--crimson)"/>
    <polygon points="17,146 296,228 296,492 17,492" fill="var(--navy)"/>
    <text x="0" y="0" transform="translate(336,300) rotate(-8.2)" font-family="Oswald, sans-serif" font-weight="600" font-size="40" fill="#fff">THE COMP &amp; PEN EXAM</text>
  </svg>

  <div class="brand-seal">Harbor Veterans Alliance</div>

  <section class="intro-panel">
    <p class="intro-lead">The Comp &amp; Pen Exam is your opportunity to present all the reasons you believe your condition is related to service to the physician.</p>
    <p class="intro-note">After your Comp &amp; Pen Exam, make sure you complete the Comp &amp; Pen Exit Survey based on your experience</p>
  </section>

  <section class="exam-summary">
    <p>If your condition is not already service-connected, be sure to talk to the examiner about what happened in service that could have led to your current condition. The examiner will review your file, including your statements, service records, and treatment records, and provide a medical opinion as to whether your condition was caused or aggravated by your military service.</p>
    <p>The examiner will be observing your movements and behavior and may perform a limited physical exam to evaluate your condition.</p>
  </section>

  <div class="section-band"><h2>THINGS TO REMEMBER FOR YOUR EXAM</h2></div>

  <section class="tips">
    <article class="tip blue">
      <div class="tip-head">
        <svg class="tip-icon" viewBox="0 0 48 40"><polygon points="6,0 48,0 42,40 0,40" fill="var(--navy)"/><ellipse cx="24" cy="18" rx="12" ry="9" fill="none" stroke="#fff" stroke-width="2.5"/><path d="M16 25 L13 32 L22 27" fill="none" stroke="#fff" stroke-width="2.5" stroke-linejoin="round"/><path d="M18 16h12M18 21h8" stroke="#fff" stroke-width="2"/></svg>
        <h3>Talk About<br>Your Service</h3>
      </div>
      <p>Talk about what happened in service that you believe caused or aggravated your condition. Try to be as specific as possible. If you are not comfortable discussing the details of an in-service event, you may point to statements you submitted to the VA previously for the examiner to reference. If you can, provide the examiner with a copy of these statements on the day of the exam.</p>
    </article>
    <article class="tip red">
      <div class="tip-head">
        <svg class="tip-icon" viewBox="0 0 48 40"><polygon points="6,0 48,0 42,40 0,40" fill="var(--crimson)"/><circle cx="21" cy="16" r="8" fill="none" stroke="#fff" stroke-width="3"/><path d="M27 22 L35 31" stroke="#fff" stroke-width="4" stroke-linecap="round"/></svg>
        <h3>Trace Your<br>Symptoms</h3>
      </div>
      <p>Discuss what symptoms you experienced immediately following your injury in service and how these symptoms have worsened over time.</p>
      <p>Your statement will help trace the start of your symptoms back to what happened during service.</p>
    </article>
    <article class="tip blue">
      <div class="tip-head">
        <svg class="tip-icon" viewBox="0 0 48 40"><polygon points="6,0 48,0 42,40 0,40" fill="var(--navy)"/><path d="M24 18 C18 13 17 7 21 6 C23 6 24 8 24 9 C24 8 25 6 27 6 C31 7 30 13 24 18Z" fill="#fff"/><path d="M10 24 H18 L26 27 H32 L38 23 V26 L32 32 H18 L10 30Z" fill="#fff"/></svg>
        <h3>Be Honest</h3>
      </div>
      <p>Be honest when describing the frequency and severity of your symptoms and how they impact your day-to-day life to the examiner; do not downplay the severity of your symptoms.</p>
      <p>Keep in mind that the examiner will be closely monitoring your movements and behavior, including your body language and the tone of your voice.</p>
    </article>
    <article class="tip blue">
      <div class="tip-head">
        <svg class="tip-icon" viewBox="0 0 48 40"><polygon points="6,0 48,0 42,40 0,40" fill="var(--navy)"/><circle cx="22" cy="8" r="4" fill="#fff"/><path d="M21 13 L18 24 L14 34 M18 24 L24 34 M20 16 L28 20 M20 16 L13 20" stroke="#fff" stroke-width="3.5" stroke-linecap="round" fill="none"/><path d="M31 12l3 3M33 9v4M35 14h4" stroke="#fff" stroke-width="2"/></svg>
        <h3>Pain</h3>
      </div>
      <p>While the exam is not meant to be painful, you may experience slight discomfort depending on the required testing.</p>
      <p>When testing your range of motion, be sure to tell the examiner AS SOON AS you begin to experience pain, as this contributes to your overall functional loss and should be considered in your rating.</p>
    </article>
    <article class="tip red">
      <div class="tip-head">
        <svg class="tip-icon" viewBox="0 0 48 40"><polygon points="6,0 48,0 42,40 0,40" fill="var(--crimson)"/><text x="24" y="32" text-anchor="middle" font-family="Oswald, sans-serif" font-weight="600" font-size="30" fill="#fff">?</text></svg>
        <h3>Ask For<br>Clarification</h3>
      </div>
      <p>Do not answer a question you do not understand. Ask for clarification if necessary. Do not talk to fill the space or time. Keep your conversation with the examiner limited to what happened in service, the frequency and severity of symptoms related to your condition, and how they impact your day-to-day life.</p>
    </article>
    <article class="tip blue">
      <div class="tip-head">
        <svg class="tip-icon" viewBox="0 0 48 40"><polygon points="6,0 48,0 42,40 0,40" fill="var(--navy)"/><rect x="12" y="6" width="14" height="5" fill="#fff"/><rect x="11" y="12" width="16" height="22" rx="2" fill="#fff"/><path d="M19 17v10M14 22h10" stroke="var(--navy)" stroke-width="3"/><rect x="29" y="17" width="8" height="16" rx="4" transform="rotate(30 33 25)" fill="#fff"/></svg>
        <h3>Medications</h3>
      </div>
      <p>If you are prescribed any medication(s) for your condition, be sure to tell the examiner the name and dosage of each medication and how often you take each. This is extremely important, because medication may mask some of your symptoms, or the use of medication(s) may be used to evaluate the severity of your condition and how much it impacts your ability to work.</p>
    </article>
  </section>
</main>
</body>
</html>
```